Creative packaging design for a juice brand

We need a creative design for a juice brand that must fit for different flavors just changing the colors or fruit design.
Our products are sold in plastic cups of 300ml opaque and transparent so the art must look good in both.
The idea is to have the same layout for different flavors in order to keep the brand identity. The only exception is the coconut water that can vary a bit (only in transparent cup).

Ex. of flavors:
- coconut water
- orange
- grape
- passion fruit
- strawberry
- guava
- peach

Use Pantones C max 5 colors (ideally 4)
Avoid overprinting as it's a limitation of the printing system
Highlight the brand logo
Any design of the fruits must cartooned or artistic
Printing area 182x55mm

NOTE TO ALL DESIGNERS:

-When working with the logo don't use the smoke effect as it doesn't look good on the offset printing. Try making a solid white or black or both instead.
- Keep in mind that for the transparent cup the colors won't look as vivid as it look in the design and the color of the juice might interfere in the color of the package. 
- It is not possible to have an overprinting. Eg. a white background + color on top
-

Kids and Youth, not limited to them.

Plastic

• Use the brand logo attached to this project
• Use your creativity and play with the background.
• No photos of any kind

```html
<!DOCTYPE html>
<html lang="en">
<head>
<meta charset="utf-8">
<title>Fruvo Juice Label Set</title>
<link href="https://fonts.googleapis.com/css2?family=Kalam:wght@400;700&family=Share+Tech+Mono&display=swap" rel="stylesheet">
<style>
  :root {
    --peach: #f9ae5b;
    --strawberry: #ee2226;
    --grape: #662d91;
    --orange: #f7941d;
    --lime: #d4f000;
    --ink: #333333;
    --paper: #ffffff;
    --line: #111111;
  }
  html, body {
    margin: 0;
    padding: 0;
    width: 1200px;
    height: 1000px;
    overflow: hidden;
    background: var(--paper);
  }
  .canvas {
    position: relative;
    width: 1200px;
    height: 1000px;
  }
  .label {
    position: absolute;
    left: 224px;
    width: 738px;
    height: 222px;
    box-sizing: border-box;
    border: 8px solid var(--flavor);
    background: var(--paper);
    overflow: hidden;
  }
  .label--peach { top: 47px; --flavor: var(--peach); --fruit-a: #fbb463; --fruit-b: #e98a2c; }
  .label--strawberry { top: 268px; --flavor: var(--strawberry); --fruit-a: #f03a3a; --fruit-b: #c8161c; }
  .label--grape { top: 490px; --flavor: var(--grape); --fruit-a: #7c3aa8; --fruit-b: #55227a; }
  .label--orange { top: 712px; --flavor: var(--orange); --fruit-a: #fa9a22; --fruit-b: #e87a0c; }

  .panel {
    position: absolute;
    top: 0;
    height: 206px;
  }
  .panel--brand { left: 0; width: 237px; }
  .panel--claims { left: 237px; width: 243px; border-left: 1px solid var(--flavor); border-right: 1px solid var(--flavor); box-sizing: border-box; }
  .panel--info { left: 480px; width: 242px; }

  .brand-name {
    position: absolute;
    top: 10px;
    left: 0;
    width: 237px;
    text-align: center;
    font-family: "Kalam", cursive;
    font-weight: 700;
    font-size: 70px;
    line-height: 1;
    color: var(--ink);
  }
  .fruit-art {
    position: absolute;
    left: 76px;
    top: 102px;
    width: 62px;
    height: 66px;
    border-radius: 50%;
    background: radial-gradient(circle at 35% 35%, var(--fruit-a), var(--fruit-b));
  }
  .flavor-name {
    position: absolute;
    top: 172px;
    left: 0;
    width: 237px;
    text-align: center;
    font-family: "Kalam", cursive;
    font-weight: 700;
    font-size: 24px;
    letter-spacing: 3px;
    color: var(--flavor);
    line-height: 30px;
  }

  .claims {
    list-style: none;
    margin: 0;
    padding: 0;
    position: absolute;
    left: 40px;
    top: 47px;
  }
  .claims li {
    position: relative;
    padding-left: 14px;
    font-family: "Kalam", cursive;
    font-weight: 700;
    font-size: 18px;
    letter-spacing: 2px;
    line-height: 31px;
    color: var(--flavor);
  }
  .claims li::before {
    content: "";
    position: absolute;
    left: 0;
    top: 13px;
    width: 7px;
    height: 7px;
    border-radius: 2px;
    background: var(--lime);
  }
  .volume {
    position: absolute;
    left: 0;
    width: 243px;
    top: 186px;
    text-align: center;
    font-family: "Share Tech Mono", monospace;
    font-size: 12px;
    line-height: 14px;
    color: var(--flavor);
    opacity: 0.6;
  }

  .info-box {
    position: absolute;
    box-sizing: border-box;
    border: 1px solid var(--line);
    border-radius: 2px;
  }
  .info-box--top { left: 31px; top: 6px; width: 187px; height: 52px; }
  .info-box--nutrition { left: 32px; top: 66px; width: 103px; height: 135px; }
  .info-box--side { left: 143px; top: 66px; width: 75px; height: 135px; }
  .nutrition-title {
    display: block;
    text-align: center;
    margin-top: 2px;
    font-family: Arial, Helvetica, sans-serif;
    font-size: 12px;
    color: var(--line);
  }
</style>
</head>
<body>
<main class="canvas">

  <section class="label label--peach">
    <div class="panel panel--brand">
      <div class="brand-name">Fruvo</div>
      <div class="fruit-art" role="img" aria-label="Cartoon peach illustration"></div>
      <div class="flavor-name">Peach</div>
    </div>
    <div class="panel panel--claims">
      <ul class="claims"><li>Vitamine C</li><li>Add Something</li><li>Add Something</li></ul>
      <div class="volume">20FL(1.25PT) 591ml</div>
    </div>
    <div class="panel panel--info">
      <div class="info-box info-box--top"></div>
      <div class="info-box info-box--nutrition"><span class="nutrition-title">Nutrition Facts</span></div>
      <div class="info-box info-box--side"></div>
    </div>
  </section>

  <section class="label label--strawberry">
    <div class="panel panel--brand">
      <div class="brand-name">Fruvo</div>
      <div class="fruit-art" role="img" aria-label="Cartoon strawberry illustration"></div>
      <div class="flavor-name">Strawberry</div>
    </div>
    <div class="panel panel--claims">
      <ul class="claims"><li>Vitamine C</li><li>Add Something</li><li>Add Something</li></ul>
      <div class="volume">20FL(1.25PT) 591ml</div>
    </div>
    <div class="panel panel--info">
      <div class="info-box info-box--top"></div>
      <div class="info-box info-box--nutrition"><span class="nutrition-title">Nutrition Facts</span></div>
      <div class="info-box info-box--side"></div>
    </div>
  </section>

  <section class="label label--grape">
    <div class="panel panel--brand">
      <div class="brand-name">Fruvo</div>
      <div class="fruit-art" role="img" aria-label="Cartoon grape bunch illustration"></div>
      <div class="flavor-name">Grape</div>
    </div>
    <div class="panel panel--claims">
      <ul class="claims"><li>Vitamine C</li><li>Add Something</li><li>Add Something</li></ul>
      <div class="volume">20FL(1.25PT) 591ml</div>
    </div>
    <div class="panel panel--info">
      <div class="info-box info-box--top"></div>
      <div class="info-box info-box--nutrition"><span class="nutrition-title">Nutrition Facts</span></div>
      <div class="info-box info-box--side"></div>
    </div>
  </section>

  <section class="label label--orange">
    <div class="panel panel--brand">
      <div class="brand-name">Fruvo</div>
      <div class="fruit-art" role="img" aria-label="Cartoon orange illustration"></div>
      <div class="flavor-name">Orange</div>
    </div>
    <div class="panel panel--claims">
      <ul class="claims"><li>Vitamine C</li><li>Add Something</li><li>Add Something</li></ul>
      <div class="volume">20FL(1.25PT) 591ml</div>
    </div>
    <div class="panel panel--info">
      <div class="info-box info-box--top"></div>
      <div class="info-box info-box--nutrition"><span class="nutrition-title">Nutrition Facts</span></div>
      <div class="info-box info-box--side"></div>
    </div>
  </section>

</main>
</body>
</html>
```